Redesign wellness clinic website

The project is redesign a wellness clinic http://www.thornleighvitality.example. The new website is to be responsive,clean,bright and a strong call to action which is to book an appointment. The logo will remain the same but the colour scheme on the website should be reflect purple white and green. I want it to be bright and cheerful and the feeling of clarity. The website shouldn't be overloaded with content but more visuals.

Target Market(s)

Anyone that has corporate wellness benefits within the downtown Toronto core. Majority of audience are professional working in Media, Telecommunications and Investments.

Industry/Entity Type

Health And Wellness

Number of Pages Required

5+ page

Font styles to use
Sans Serif

Colors
ffffff
886aae
acd036

Requirements
Must have
• -Strong call to action which is book an appointment like this page https://www.kestrelmotion.example/
• -Services provided icons on the page like https://www.brightpathvitalityhouse.example/
• - Pictures of a good visualizing a fit and healthy life
• - Strong ratings from Quorva, Zintrel, PostMaz, similar to this website http://www.summitbalancehealth.example/our-team-professionals/
• - Bright and clear
Should not have
• -No black and white images (redo our pictures)
• -Dark themes

```html
<!DOCTYPE html>
<html lang="en">
<head>
<meta charset="utf-8">
<title>Thornleigh Vitality Centre – Physiotherapy</title>
<link href="https://fonts.googleapis.com/css2?family=Fira+Sans:wght@300;400;500;600&display=swap" rel="stylesheet">
<style>
:root{
  --purple:#886aae;
  --purple-dark:#7a5ea1;
  --green:#acd036;
  --white:#ffffff;
  --ink:#2f2f33;
  --text:#55565b;
  --muted:#8a8b90;
  --line:#e4e4e6;
  --panel:#f4f4f5;
  --nav:#eeeeef;
}
*{box-sizing:border-box;margin:0;padding:0}
html,body{width:1200px;height:3261px;overflow:hidden}
body{position:relative;background:var(--white);font-family:"Fira Sans",Arial,sans-serif;color:var(--text);font-size:13px;line-height:1.55}
a{color:var(--purple);text-decoration:underline}
.abs{position:absolute}

/* header */
.site-header{top:0;left:0;width:1200px;height:92px}
.brand{left:174px;top:22px;display:flex;align-items:center;gap:10px}
.brand-mark{width:40px;height:40px;border-radius:50%;background:var(--purple)}
.brand-name{font-size:14px;font-weight:600;color:var(--purple);line-height:1.2}
.brand-phone{font-size:9px;color:var(--muted);font-weight:400;display:block}
.btn{display:flex;align-items:center;justify-content:center;gap:8px;height:37px;border-radius:19px;color:var(--white);font-size:13px;font-weight:500;text-decoration:none}
.btn-call{left:648px;top:27px;width:185px;background:var(--green)}
.btn-book{left:843px;top:27px;width:184px;background:var(--purple)}

.main-nav{top:92px;left:0;width:1200px;height:35px;background:var(--nav);border-top:1px solid #e2e2e4}
.main-nav ul{list-style:none;position:absolute;left:182px;top:0;display:flex;gap:24px;height:35px;align-items:center}
.main-nav li{font-size:12.5px;color:#55565b}
.search{position:absolute;left:859px;top:6px;width:168px;height:23px;border-radius:12px;background:var(--white);border:1px solid #dddde0;font-size:11.5px;color:#aaa;display:flex;align-items:center;gap:7px;padding-left:12px}

/* hero */
.hero{top:127px;left:0;width:1200px;height:286px;overflow:hidden}
.hero-photo{position:absolute;inset:0;background:linear-gradient(90deg,#ffffff 0%,#f7f8fa 30%,#e6ebf0 55%,#d7c3b3 72%,#c9cfd8 88%,#e8ecf0 100%)}
.hero-title{position:absolute;left:272px;top:70px;text-align:center;width:130px}
.hero-mark{width:44px;height:44px;border-radius:50%;background:var(--purple);margin:0 auto 12px;border:5px solid var(--green)}
.hero-title h1{font-size:22px;font-weight:500;color:var(--purple)}
.hero-wave{position:absolute;left:0;bottom:0}

/* sections */
h2{font-size:22px;font-weight:500;color:var(--ink);line-height:1.2}
h3{font-size:15px;font-weight:500;color:var(--ink);margin-bottom:10px}
.divider{left:174px;width:852px;height:1px;background:var(--line)}

.physio{top:467px;left:174px;width:852px;height:260px}
.physio-photo{position:absolute;left:0;top:2px;width:413px;height:255px;background:linear-gradient(135deg,#e8d8c9,#c9b7a4 45%,#e3c8b6 70%,#b8b2ad)}
.physio-text{position:absolute;left:437px;top:0;width:415px}
.physio-text h2{margin-bottom:12px}
.physio-text p{margin-bottom:14px}

.athletic{top:810px;left:174px;width:852px;text-align:center}
.athletic > p{width:700px;margin:12px auto 0}
.cards{display:flex;gap:24px;margin-top:30px}
.card{width:268px;height:257px;background:var(--panel);padding:36px 24px 0}
.card svg{display:block;margin:0 auto 22px}
.card h4{font-size:15px;font-weight:500;color:var(--ink);margin-bottom:10px}
.card p{font-size:12.5px;line-height:1.6}
.athletic .assoc{margin-top:30px}

.orthotics{top:1303px;left:174px;width:852px}
.orthotics h2{margin-bottom:20px}
.cols{display:flex;gap:32px}
.col{width:410px}
.col-right{width:410px}
.bullets{list-style:none;margin:12px 0}
.bullets li{position:relative;padding-left:22px;margin-bottom:4px}
.bullets li::before{content:"";position:absolute;left:3px;top:6px;width:8px;height:8px;border:2px solid var(--green);transform:rotate(45deg)}

.bracing{top:1662px;left:174px;width:852px}
.bracing h2{margin-bottom:22px}
.bracing p{margin-bottom:14px}
.links a{display:block;line-height:1.7}

.compression{top:2247px;left:174px;width:852px}
.compression h2{margin-bottom:12px}
.compression p{margin-bottom:18px}

.prices{top:2542px;left:174px;width:852px}
.prices h2{margin-bottom:12px}
.prices .note{font-size:12px;line-height:1.5}
.prices h3{margin-top:26px;margin-bottom:28px}
.price-row{display:flex;justify-content:space-between;font-size:12.5px;padding:6px 0;border-bottom:1px solid var(--line)}

/* newsletter band */
.band{top:2798px;left:0;width:1200px;height:78px;background:var(--panel)}
.newsletter{position:absolute;left:174px;top:18px;display:flex;align-items:center;gap:12px}
.newsletter strong{font-size:15px;font-weight:500;color:var(--ink);line-height:1.1;width:90px}
.email{width:170px;height:31px;border-radius:16px;background:var(--white);font-size:12px;color:#aaa;padding:7px 14px;margin-left:8px}
.subscribe{height:31px;border-radius:16px;background:var(--green);color:var(--white);font-size:12.5px;padding:7px 18px;margin-left:-30px}
.band-split{position:absolute;left:640px;top:14px;width:1px;height:50px;background:#dcdcde}
.referral{position:absolute;left:686px;top:18px;display:flex;align-items:center;gap:14px}
.referral strong{font-size:15px;font-weight:500;color:var(--ink);line-height:1.2;width:250px}

/* footer */
.site-footer{top:2876px;left:0;width:1200px;height:385px;background:var(--purple);color:var(--white)}
.site-footer h5{font-size:15px;font-weight:500;margin-bottom:14px}
.f-col{position:absolute;top:40px;font-size:12px;line-height:1.5}
.f-contact{left:174px;width:200px}
.f-hours{left:391px;width:200px}
.f-tweets{left:613px;width:200px}
.f-award{left:826px;width:200px;text-align:center}
.btn-footer{width:185px;margin-top:16px;background:var(--green);height:37px}
.tweet{display:flex;gap:10px;margin-bottom:14px}
.tweet-avatar{width:46px;height:46px;border-radius:50%;background:linear-gradient(135deg,#c9b8dc,#9f86c0);flex:none}
.tweet small{font-size:11px;opacity:.9}
.badge{width:90px;height:110px;margin:0 auto 12px;background:#f08a24;border-radius:6px 6px 45px 45px}
.social{position:absolute;left:560px;top:292px;display:flex;gap:12px}
.social span{width:34px;height:34px;border-radius:50%;border:2px solid var(--white)}
.copyright{position:absolute;left:0;width:1200px;top:344px;text-align:center;font-size:11.5px;border-top:1px solid rgba(255,255,255,.25);padding-top:14px}
</style>
</head>
<body>

<header class="site-header abs">
  <div class="brand abs">
    <span class="brand-mark"></span>
    <span class="brand-name">Thornleigh Vitality Centre<span class="brand-phone">Call 416 555 0172</span></span>
  </div>
  <a class="btn btn-call abs" href="#">
    <svg width="14" height="14" viewBox="0 0 24 24" fill="#fff"><path d="M6.6 10.8a15.1 15.1 0 0 0 6.6 6.6l2.2-2.2a1 1 0 0 1 1-.25 11.4 11.4 0 0 0 3.6.57 1 1 0 0 1 1 1V20a1 1 0 0 1-1 1A17 17 0 0 1 3 4a1 1 0 0 1 1-1h3.5a1 1 0 0 1 1 1c0 1.25.2 2.45.57 3.57a1 1 0 0 1-.25 1z"/></svg>
    Call Us : 416-555-0172</a>
  <a class="btn btn-book abs" href="#">
    <svg width="14" height="14" viewBox="0 0 24 24" fill="#fff"><path d="M7 2v2H5a2 2 0 0 0-2 2v14a2 2 0 0 0 2 2h14a2 2 0 0 0 2-2V6a2 2 0 0 0-2-2h-2V2h-2v2H9V2zM5 9h14v11H5z"/></svg>
    Book An Appointment</a>
</header>

<nav class="main-nav abs">
  <ul>
    <li>Home</li><li>Fees &amp; Services</li><li>Our Staff</li><li>Bios</li><li>News &amp; Updates</li><li>Corporate Wellness</li><li>Forms</li><li>Contact</li>
  </ul>
  <div class="search">
    <svg width="12" height="12" viewBox="0 0 24 24" fill="none" stroke="#999" stroke-width="2.5"><circle cx="10" cy="10" r="7"/><path d="M15 15l6 6"/></svg>Search
  </div>
</nav>

<section class="hero abs">
  <div class="hero-photo" role="img" aria-label="Two smiling runners jogging outdoors in bright sportswear"></div>
  <div class="hero-title">
    <div class="hero-mark"></div>
    <h1>Physiotherapy</h1>
  </div>
  <svg class="hero-wave" width="1200" height="120" viewBox="0 0 1200 120">
    <path d="M0 55 C300 130 700 130 1200 25 L1200 120 L0 120Z" fill="var(--green)"/>
    <path d="M0 85 C350 150 800 120 1200 40 L1200 120 L0 120Z" fill="var(--purple)"/>
    <path d="M0 98 C380 160 820 120 1200 62 L1200 120 L0 120Z" fill="#fff"/>
  </svg>
</section>

<section class="physio abs">
  <div class="physio-photo" role="img" aria-label="Physiotherapist stretching a patient's leg on a treatment table"></div>
  <div class="physio-text">
    <h2>Physiotherapy</h2>
    <p>Physiotherapy is a drug-free health care practice. Physiotherapists work in partnership with individuals of all ages to break down the barriers to physical function whether that means working with patients pre and post surgery, helping people come back from illness and chronic disease, injury, industrial and motor vehicle accidents and age related conditions. Physiotherapists also play an important role in health promotion and disease prevention. We now offer pelvic floor rehabilitation for women with pelvic floor weakness, incontinence, and low grade prolapse.</p>
    <p>Provincial Physio Guild <a href="#">www.physioguild.example</a></p>
  </div>
</section>

<div class="divider abs" style="top:765px"></div>

<section class="athletic abs">
  <h2>Athletic Therapy</h2>
  <p>Athletic Therapy is a profession that provides a variety of services that assist active people who have sustained or could sustain an injury. These services fall into three main areas:</p>
  <div class="cards">
    <div class="card">
      <svg width="44" height="44" viewBox="0 0 44 44" fill="none" stroke="var(--purple)" stroke-width="2"><circle cx="22" cy="9" r="5"/><path d="M8 20h28M22 20v10M15 38l7-8 7 8M12 20v-4M32 20v-4"/></svg>
      <h4>Prevention</h4>
      <p>Athletic therapists employ many strategies to help active individuals avoid or minimize the possibility of injury</p>
    </div>
    <div class="card">
      <svg width="44" height="44" viewBox="0 0 44 44" fill="none" stroke="var(--purple)" stroke-width="2"><path d="M22 36S8 27 8 17a7 7 0 0 1 14-2 7 7 0 0 1 14 2c0 10-14 19-14 19z"/><path d="M22 18v8M18 22h8"/></svg>
      <h4>Immediate care</h4>
      <p>Many musculoskeletal orthopedic injuries require immediate expert care, including injury assessment, first aid and transition into the health care system.</p>
    </div>
    <div class="card">
      <svg width="44" height="44" viewBox="0 0 44 44" fill="none" stroke="var(--purple)" stroke-width="2"><circle cx="24" cy="8" r="4"/><path d="M24 14v12l-6 12M24 26l6 12M16 20h16"/></svg>
      <h4>Rehabilitation</h4>
      <p>Post-injury, athletic therapy focuses on preparing active individuals to re-establish their pre-injury lifestyle through physical reconditioning, hands-on therapy and other rehabilitative techniques.</p>
    </div>
  </div>
  <p class="assoc">National Athletic Therapy Council <a href="#">www.motioncarers.example</a></p>
</section>

<div class="divider abs" style="top:1261px"></div>

<section class="orthotics abs">
  <h2>Orthotics</h2>
  <div class="cols">
    <div class="col">
      <h3>What is a Custom Orthotic?</h3>
      <p>A custom orthotic is a device designed to align the foot and ankle into the most anatomically efficient position. They look like insoles, but are biomechanical medical appliances that are custom made to correct your specific foot imbalance which will help reduce stress and strain on your body. The plastic body of the custom orthotic helps to re-align the foot by redirecting and reducing certain motion that takes place during walking.</p>
    </div>
    <div class="col-right">
      <h3>Who Needs Them?</h3>
      <p>The symptoms of poor foot mechanics can include any one of the following:</p>
      <ul class="bullets">
        <li>Localized foot pain</li><li>Bunions, hammer toes</li><li>Arch/heel pain</li><li>Leg/knee pain</li><li>Hip or back pain - even neck pain</li>
      </ul>
      <a href="#">http://www.archformlab.example/</a>
    </div>
  </div>
</section>

<div class="divider abs" style="top:1620px"></div>

<section class="bracing abs">
  <h2>Bracing</h2>
  <h3>Why Brace?</h3>
  <p>Braces and splints can be useful for acute injuries, chronic conditions, and the prevention of injury. There is good evidence to support the use of some braces and splints. They have a relatively low cost, and no adverse effects.</p>
  <h3>Types of Braces</h3>
  <p style="margin-bottom:0">There are four main kinds of braces:</p>
  <ul class="bullets">
    <li>Prophylactic (say: "pro-fa-lack-tick") braces. These are designed to protect knees from injuries during contact sports like football.</li>
    <li>Functional braces. These give support to knees that have already been injured.</li>
    <li>Rehabilitative braces. These limit harmful knee movement while a knee is healing after an injury or surgery.</li>
    <li>Unloader/offloader braces. These are designed to provide relief to people who have arthritis in their knees.</li>
  </ul>
  <p style="margin-bottom:0">Bracing Can be used for the following conditions:</p>
  <ul class="bullets">
    <li>ACL Reconstruction</li><li>Tennis/Golfers Elbow</li><li>Knee Osteoarthritis</li><li>Carpal Tunnel</li>
  </ul>
  <div class="links">
    <a href="#">https://www.bracewell.example/</a>
    <a href="#">http://www.kinhold.example/</a>
    <a href="#">https://www.jointly.example/</a>
  </div>
</section>

<div class="divider abs" style="top:2207px"></div>

<section class="compression abs">
  <h2>Compression Stockings</h2>
  <p>Heavy and tired legs and swollen ankles are signs of chronic venous insufficiency, which is a serious disease with real consequences. Around 15 percent of the population currently suffers from venous diseases. If you find that your shoes are getting tight during the day, this could be a visible sign for a venous weakness. Wearing compression stocking is key with the treatment of venous disorders. This treatment is prescribed by a physician to treat phlebitis, thrombosis and aftercare following surgery, sclerotherapy and any other forms of varicose vein treatment, and also to relieve all conditions of chronic venous disease (heavy legs, varicose veins, edemas, leg ulcers). It can also be prescribed to prevent venous issues during pregnancy and long distance travel. If no contraindications like severe arterial insufficiency are present, compression stockings of lower pressure can be purchased without prescription.</p>
  <a href="#">https://www.veloxsock.example</a>
</section>

<div class="divider abs" style="top:2500px"></div>

<section class="prices abs">
  <h2>Price List &amp; Service</h2>
  <p class="note">*All prices include HST (unless otherwise stated)<br>* Some services may be covered by Private Insurance, Auto Insurance or WPIB. (Click here to download a printable version)</p>
  <h3>Physiotherapy/ Athletic Therapy</h3>
  <div class="price-row"><span>Initial evaluation</span><span>$80.00</span></div>
  <div class="price-row"><span>Subsequent visits 20 min / 30 min/ 40 min / 60 min</span><span>$60.00 / $82.50 / $100 / $120</span></div>
</section>

<section class="band abs">
  <div class="newsletter">
    <svg width="34" height="30" viewBox="0 0 34 30" fill="none" stroke="var(--ink)" stroke-width="2"><rect x="2" y="6" width="30" height="22"/><path d="M2 6l15 12 15-12M8 2h18"/></svg>
    <strong>Subscribe Newsletter</strong>
    <span class="email">Email Address</span>
    <span class="subscribe">Subscribe</span>
  </div>
  <div class="band-split"></div>
  <div class="referral">
    <svg width="34" height="32" viewBox="0 0 34 32" fill="none" stroke="var(--ink)" stroke-width="2"><rect x="3" y="10" width="28" height="20"/><path d="M3 10l14-8 14 8M10 18h14M10 23h10"/></svg>
    <strong>Ask one of our associates about our Referral Reward Program!</strong>
    <svg width="26" height="16" viewBox="0 0 26 16" fill="none" stroke="var(--ink)" stroke-width="2"><path d="M0 8h24M17 1l7 7-7 7"/></svg>
  </div>
</section>

<footer class="site-footer abs">
  <div class="f-col f-contact">
    <h5>Contact Us</h5>
    <p>Thornleigh Vitality Centre<br>48 Marlow Avenue East, Suite 210<br>Toronto, Ontario, M4W 2K9</p>
    <p style="margin-top:12px">Phone: 416-555-0172<br>Fax: 416-555-0188</p>
    <a class="btn btn-footer" href="#">Book An Appointment</a>
  </div>
  <div class="f-col f-hours">
    <h5>Hours of Operation</h5>
    <p>We are open for business at 7:30 am. Open 7 days a week!</p>
    <p style="margin-top:12px">Monday to Friday:<br>7:30am - 8pm</p>
    <p style="margin-top:12px">Saturday to Sunday:<br>10am - 5pm</p>
  </div>
  <div class="f-col f-tweets">
    <h5>Our Tweets</h5>
    <div class="tweet">
      <span class="tweet-avatar" role="img" aria-label="Profile picture"></span>
      <p>Thornleigh Vitality<br>@ThornleighVital<br>http://lnk.example/7qe4210Tk<br><small>30 Aug 2017 &nbsp;&nbsp;&nbsp;&nbsp;&nbsp;&nbsp;&nbsp; ♡ &nbsp;⇄</small></p>
    </div>
    <div class="tweet">
      <span class="tweet-avatar" role="img" aria-label="Profile picture"></span>
      <p>Thornleigh Vitality<br>@ThornleighVital<br>http://lnk.example/7qe4210Tk<br><small>30 Aug 2017 &nbsp;&nbsp;&nbsp;&nbsp;&nbsp;&nbsp;&nbsp; ♡ &nbsp;⇄</small></p>
    </div>
  </div>
  <div class="f-col f-award">
    <div class="badge" role="img" aria-label="Community choice award badge"></div>
    <p>Thornleigh Vitality Centre is ranked as a top Wellness Centre in Toronto ON<br>Verified by Bookwise.example</p>
  </div>
  <div class="social"><span></span><span></span></div>
  <p class="copyright">Copyright © 2017 Thornleigh Vitality Centre</p>
</footer>

</body>
</html>
```